High end Electrical/home automation Business Card

Need a card for a high end electrical and home automation company utilising the existing logo.
Phone
Email
Website

Like black look with raised detail. Don’t necessarily need to keep colour of logo it could be made grayscale or white etc

Target Market(s)

High end clients

Contact Information for Business Card

Northwell Electrical

Requirements
Must have
• Logo, phone, email, website, address

High end look
Nice to have
• Black background card
Raised font
Should not have
• Lots of colour

```html
<!DOCTYPE html>
<html lang="en">
<head>
<meta charset="utf-8">
<title>Northwell Electrical – Business Card</title>
<link rel="stylesheet" href="https://fonts.googleapis.com/css2?family=Lato:wght@400;700&family=Oswald:wght@500&display=swap">
<style>
  :root {
    --backdrop: #2b2b2b;
    --card: #323232;
    --card-edge: #3a3a3a;
    --foil: #cfcfcf;
    --ink: #f2f2f2;
    --rule: #bdbdbd;
  }
  * { margin: 0; padding: 0; box-sizing: border-box; }
  html, body {
    width: 1133px;
    height: 1200px;
    overflow: hidden;
    background: var(--backdrop);
  }
  .canvas {
    position: relative;
    width: 1133px;
    height: 1200px;
  }
  .card {
    position: absolute;
    left: 244px;
    width: 656px;
    height: 362px;
    background: var(--card);
    border: 1px solid var(--card-edge);
  }
  .card--front { top: 190px; }
  .card--back  { top: 626px; }

  .brand {
    position: absolute;
    left: 0;
    right: 0;
    top: 0;
    bottom: 0;
    display: flex;
    align-items: center;
    justify-content: center;
    gap: 14px;
  }
  .brand__dot {
    width: 16px;
    height: 16px;
    border-radius: 50%;
    background: var(--foil);
  }
  .brand__name {
    font-family: "Lato", sans-serif;
    font-weight: 700;
    font-size: 36px;
    letter-spacing: -0.5px;
    color: var(--foil);
  }

  .holder {
    position: absolute;
    right: 380px;
    top: 156px;
    text-align: right;
  }
  .holder__name {
    font-family: "Oswald", sans-serif;
    font-weight: 500;
    font-size: 28px;
    line-height: 1;
    letter-spacing: 0.5px;
    color: var(--ink);
  }
  .holder__title {
    font-family: "Lato", sans-serif;
    font-size: 15px;
    line-height: 1.3;
    color: var(--ink);
    margin-top: 3px;
  }
  .divider {
    position: absolute;
    left: 302px;
    top: 122px;
    width: 1px;
    height: 116px;
    background: var(--rule);
  }
  .contact {
    position: absolute;
    left: 325px;
    top: 122px;
    font-family: "Lato", sans-serif;
    font-size: 16.5px;
    line-height: 21px;
    color: var(--ink);
    font-style: normal;
  }
  .contact__address { margin-bottom: 11px; }
</style>
</head>
<body>
  <main class="canvas">
    <section class="card card--front" aria-label="Card front">
      <div class="brand">
        <span class="brand__dot" aria-hidden="true"></span>
        <span class="brand__name">Northwell Electrical</span>
      </div>
    </section>

    <section class="card card--back" aria-label="Card back">
      <div class="holder">
        <p class="holder__name">DANIEL HARTLEY</p>
        <p class="holder__title">President</p>
      </div>
      <div class="divider" aria-hidden="true"></div>
      <address class="contact">
        <p class="contact__address">4128 Alder Ridge Road<br>Anchorage, Alaska 99515</p>
        <p>P. 555-204-7731</p>
        <p>info@northwellelectrical.com</p>
        <p>www.northwellelectrical.com</p>
      </address>
    </section>
  </main>
</body>
</html>
```